Anzeigengestaltung für Handwerksbetrieb
Zielgruppe
Handwerksbetrieb
Maler und Lackierer
Wir möchten mit einem auffälligem und einprägsamen Werbeslogen unsere Bekanntheit in unserer Stadt verstärken. Dieses Design samt Slogan soll künftig alle unsere Werbeaktionen begleiten.
Aufgabenstellung
Der Werbeslogan : 'Wir machen Braunschweig bunter' muss enthalten sein.
Ein optischer Zusammenhang zur Stadt Braunschweig wie z.B. Silouette der Stadt wären wünschenswert.
Gerne bunt und auffallend gestaltet.

```html
<!DOCTYPE html>
<html lang="de">
<head>
<meta charset="utf-8">
<title>Malerbetrieb Hollmann – Wir machen Braunschweig bunter</title>
<link href="https://fonts.googleapis.com/css2?family=Anton&family=Kaushan+Script&family=Montserrat:wght@500;700&display=swap" rel="stylesheet">
<style>
  :root{
    --brand-red:#7e1a22;
    --brand-red-light:#9a3a36;
    --gold:#c9b078;
    --gold-pale:#efe6d2;
    --white:#ffffff;
    --sky-top:#4e3148;
    --sky-mid:#c5654a;
    --sky-glow:#eea45a;
    --street-dark:#221c26;
  }
  *{margin:0;padding:0;box-sizing:border-box}
  html,body{width:1200px;height:1200px;overflow:hidden;background:var(--brand-red)}
  .ad{position:relative;width:1200px;height:1200px;overflow:hidden;background:var(--brand-red)}
  .ad__shapes{position:absolute;inset:0;width:1200px;height:1200px}
  .brand{position:absolute;left:0;width:560px;top:70px;text-align:center;color:var(--gold);
    font-family:"Montserrat",sans-serif;font-weight:500}
  .brand__mark{width:120px;height:120px;border-radius:50%;background:var(--gold);margin:0 auto 34px}
  .brand__name{font-size:74px;line-height:1;letter-spacing:2px}
  .brand__trade{font-size:30px;letter-spacing:17px;margin-top:16px;padding-left:17px}
  .brand__rule{width:340px;height:1px;background:var(--gold);margin:18px auto 14px;opacity:.7}
  .brand__tagline{font-size:15px;letter-spacing:1px}
  .slogan{position:absolute;left:75px;top:478px}
  .slogan__line{font-family:"Anton",sans-serif;color:var(--white);font-size:104px;line-height:117px;
    text-transform:uppercase;letter-spacing:-1px}
  .slogan__accent{font-family:"Kaushan Script",cursive;color:var(--gold);font-size:118px;line-height:1;
    margin-top:-6px}
  .divider{position:absolute;left:75px;top:910px;width:231px;height:5px;background:var(--white)}
  .contacts{position:absolute;left:75px;top:975px;list-style:none}
  .contacts__item{display:flex;align-items:center;height:40px;margin-bottom:25px;
    font-family:"Montserrat",sans-serif;font-weight:700;font-size:26px;color:var(--white)}
  .contacts__icon{width:36px;height:36px;margin-right:27px;flex:none}
</style>
</head>
<body>
<main class="ad">
  <svg class="ad__shapes" viewBox="0 0 1200 1200" aria-hidden="false">
    <defs>
      <linearGradient id="skyline" x1="0" y1="0" x2="0" y2="1">
        <stop offset="0" stop-color="var(--sky-top)"/>
        <stop offset=".35" stop-color="var(--sky-mid)"/>
        <stop offset=".55" stop-color="var(--sky-glow)"/>
        <stop offset=".7" stop-color="var(--street-dark)"/>
        <stop offset="1" stop-color="#3a2a2c"/>
      </linearGradient>
      <linearGradient id="sheen" x1="0" y1="0" x2="1" y2="0">
        <stop offset="0" stop-color="var(--brand-red)" stop-opacity="0"/>
        <stop offset="1" stop-color="var(--brand-red-light)"/>
      </linearGradient>
      <linearGradient id="goldWedge" x1="0" y1="0" x2="0" y2="1">
        <stop offset="0" stop-color="#d9c596"/>
        <stop offset=".6" stop-color="var(--gold-pale)"/>
        <stop offset="1" stop-color="#e2d4b2"/>
      </linearGradient>
    </defs>
    <polygon class="ad__scene" role="img" aria-label="Illustration: Braunschweiger Häuserzeile mit erleuchteten Fenstern vor orange-violettem Abendhimmel"
      points="823,0 1200,0 1200,1200 540,1200" fill="url(#skyline)"/>
    <polygon class="ad__sheen" points="617,34 790,34 668,545 617,545" fill="url(#sheen)" opacity=".8"/>
    <polygon class="ad__wedge" points="610,899 540,1200 773,1200" fill="url(#goldWedge)"/>
  </svg>

  <header class="brand">
    <div class="brand__mark"></div>
    <div class="brand__name">Hollmann</div>
    <div class="brand__trade">MALERBETRIEB</div>
    <div class="brand__rule"></div>
    <div class="brand__tagline">HOMEDESIGN BRAUNSCHWEIG</div>
  </header>

  <h1 class="slogan">
    <div class="slogan__line">Wir machen</div>
    <div class="slogan__line">Braunschweig</div>
    <div class="slogan__accent">Bunter</div>
  </h1>

  <div class="divider"></div>

  <ul class="contacts">
    <li class="contacts__item">
      <svg class="contacts__icon" viewBox="0 0 36 36"><circle cx="18" cy="18" r="18" fill="var(--gold)"/></svg>
      malerbetriebhollmann
    </li>
    <li class="contacts__item">
      <svg class="contacts__icon" viewBox="0 0 36 36">
        <circle cx="18" cy="18" r="18" fill="var(--gold)"/>
        <g fill="none" stroke="var(--brand-red)" stroke-width="1.8">
          <circle cx="18" cy="18" r="10"/>
          <ellipse cx="18" cy="18" rx="4.5" ry="10"/>
          <line x1="8" y1="18" x2="28" y2="18"/>
          <line x1="10" y1="13" x2="26" y2="13"/>
          <line x1="10" y1="23" x2="26" y2="23"/>
        </g>
      </svg>
      malerbetriebhollmann.example
    </li>
  </ul>
</main>
</body>
</html>
```